Coral Wing Flights business card

I need a business card designed based on our logo -- designed by Pixel Guild designers.

The logo is to be taken from our web site at www.coralwingflights.com.au

I need to have this card designed quickly as its needed for business meetings
Updates

Hi Designers, Please see my updated brief for my business card. I have attached logo images and a brochure for inspiration... Regards, Marco Debellis Coral Wing Flights

Target Market(s)

Hotel owners and operators (concierge) and tourists to Australia

Industry/Entity Type

Business

Font styles to use
Sans Serif

Colors
84abd2
3176b5
85abd2
cedeec

Requirements
Must have
• Utilise our logo. Found on our web page www.coralwingflights.com.au

SIDE 1
Must have my name: Marco Debellis
Title:Owner
Phone number: 1300 418 295
Mobile:0431267589

SIDE 2
LOGO
PREPARE TO BE AMAZED! (see attached brochure for information and font style)
Nice to have
• Something that reflects aviation and tour with a light aircraft

```html
<!DOCTYPE html>
<html lang="en">
<head>
<meta charset="utf-8">
<title>Coral Wing Flights – Business Card</title>
<link rel="stylesheet" href="https://fonts.googleapis.com/css2?family=Jost:wght@400;500&family=Oswald:wght@600&display=swap">
<style>
  :root {
    --sky: #41a9d7;
    --sky-light: #6cc1e6;
    --sky-deep: #2f96c8;
    --plane-tone: #c9e6f4;
    --plane-shade: #8fcbe8;
    --ink-blue: #1b86b8;
    --white: #ffffff;
    --paper: #f3f5f7;
    --logo-ink: #3a3a3a;
  }
  * { box-sizing: border-box; margin: 0; padding: 0; }
  html, body { width: 900px; height: 1200px; overflow: hidden; }
  body {
    background: var(--paper);
    font-family: "Jost", Arial, sans-serif;
    position: relative;
  }
  .card {
    position: absolute;
    left: 90px;
    width: 720px;
    height: 400px;
    overflow: hidden;
    background: var(--sky);
    box-shadow: 0 6px 18px rgba(0,0,0,0.12);
  }
  .card--front { top: 150px; }
  .card--back  { top: 650px; }

  .sky-backdrop {
    position: absolute;
    inset: 0;
    background: linear-gradient(160deg, var(--sky-light) 0%, var(--sky) 45%, var(--sky-deep) 100%);
  }
  .plane-photo {
    position: absolute;
    border-radius: 50%;
    background: radial-gradient(ellipse at 55% 50%, var(--plane-tone) 0%, var(--plane-shade) 45%, rgba(65,169,215,0) 72%);
    opacity: 0.85;
  }
  .card--front .plane-photo { left: 175px; top: 60px; width: 560px; height: 240px; }
  .card--back  .plane-photo { left: 200px; top: 0;    width: 540px; height: 225px; }

  /* Front */
  .brand-name--front {
    position: absolute;
    left: 42px;
    top: 78px;
    font-size: 38px;
    font-weight: 500;
    color: var(--white);
    letter-spacing: 0.5px;
  }
  .name-plate {
    position: absolute;
    left: 0;
    top: 260px;
    width: 404px;
    height: 84px;
    background: var(--white);
    padding: 7px 0 0 40px;
  }
  .person-name {
    font-size: 32px;
    font-weight: 400;
    color: var(--ink-blue);
    line-height: 1.15;
    letter-spacing: 0.5px;
  }
  .person-title {
    font-size: 25px;
    font-weight: 400;
    color: var(--ink-blue);
    line-height: 1.3;
  }
  .contact-line {
    position: absolute;
    left: 40px;
    top: 352px;
    display: flex;
    align-items: center;
    gap: 6px;
    color: var(--white);
    font-size: 24px;
    letter-spacing: 1px;
  }
  .contact-line svg { width: 22px; height: 22px; flex: none; }
  .contact-line .mobile { margin-left: 14px; }

  /* Back */
  .card--back .sky-backdrop { bottom: 176px; }
  .tagline {
    position: absolute;
    left: 38px;
    top: 56px;
    font-family: "Oswald", Impact, sans-serif;
    font-weight: 600;
    font-size: 36px;
    letter-spacing: 1px;
    color: var(--white);
    text-transform: uppercase;
  }
  .logo-panel {
    position: absolute;
    left: 0;
    top: 226px;
    width: 100%;
    height: 150px;
    background: var(--white);
    display: flex;
    align-items: center;
    justify-content: center;
  }
  .brand-name--back {
    font-size: 46px;
    font-weight: 500;
    color: var(--logo-ink);
    letter-spacing: 0.5px;
  }
  .base-strip {
    position: absolute;
    left: 0;
    bottom: 0;
    width: 100%;
    height: 24px;
    background: var(--sky);
  }
</style>
</head>
<body>

  <section class="card card--front" aria-label="Business card front">
    <div class="sky-backdrop"></div>
    <div class="plane-photo" role="img" aria-label="Photo of an airliner climbing after take-off against a blue sky"></div>
    <div class="brand-name brand-name--front">Coral Wing Flights</div>
    <div class="name-plate">
      <p class="person-name">Marco Debellis</p>
      <p class="person-title">Owner</p>
    </div>
    <div class="contact-line">
      <svg viewBox="0 0 24 24" aria-hidden="true">
        <circle cx="12" cy="12" r="10.5" fill="none" stroke="#fff" stroke-width="1.6"/>
        <path d="M8.4 6.8c.4-.4 1-.4 1.3 0l1.3 1.6c.3.4.3.9 0 1.2l-.8.8c.6 1.3 1.6 2.4 2.9 3l.8-.8c.3-.3.9-.3 1.2 0l1.6 1.3c.4.3.4.9 0 1.3l-.9.9c-.6.6-1.5.7-2.3.3-2.6-1.2-4.6-3.3-5.8-5.8-.4-.8-.2-1.7.4-2.3z" fill="#fff"/>
      </svg>
      <span>1300 418 295</span>
      <svg class="mobile" viewBox="0 0 24 24" aria-hidden="true">
        <rect x="7" y="2" width="10" height="20" rx="2" fill="#fff"/>
        <rect x="9" y="5" width="6" height="11" fill="#41a9d7"/>
        <circle cx="12" cy="19" r="1.1" fill="#41a9d7"/>
      </svg>
      <span>0431267589</span>
    </div>
  </section>

  <section class="card card--back" aria-label="Business card back">
    <div class="sky-backdrop"></div>
    <div class="plane-photo" role="img" aria-label="Photo of an airliner flying overhead against a blue sky"></div>
    <h1 class="tagline">Prepare to be amazed</h1>
    <div class="logo-panel">
      <span class="brand-name brand-name--back">Coral Wing Flights</span>
    </div>
    <div class="base-strip"></div>
  </section>

</body>
</html>
```